Counseling Practice Business Card

I need a professional looking business card incorporating my new logo that was just completed. Card needs to incorporate my name and title, description of my specialty, my address, my phone number, my fax number, my email and my website URL. I need to be able to choose design on/with different paper colors and textures.
I do not have a lot of business card ideas so I am open to anything but I want bold,sharp, clear card without additional designs other than my logo (see attached file info). I am open to different color backgrounds or paper colors including black. I do not like traditional brackets around area codes in phone number or dashes between numbers in phone number. Am open to other ways of presenting including periods between numbers as appropriate. I do not know enough to know what I like yet but I want card to coordinate and work together with my logo. My practice emphasizes natural mental health interventions so any use of color (with background paper color or the blue and green in my logo) that elicits nature is nice. In addition to black, any natural brown or wood looking background might be desirable also. Most of the offerings so far look very similar and boring.

Target Market(s)

Potential therapy clients and other professionals

Contact Information for Business Card

Card information:
Marcus T. Whitfield, Ph.D.
Licensed Clinical Psychologist
Integrative Health Coach
4812 Ferndale Pkwy NW
Suite 730
Ashford, GA 30417
(770) 555-0142 phone
(770) 555-0186 fax
drmarcuswhitfield@kelvora.com
pathbloomcounseling.com

Font styles to use
Serif
Sans Serif
Other font styles liked:
• anything that you think looks crisp, clear and easily readable

Requirements
Must have
• Any color used should coordinate with my logo design (see attached files).
• Card should be printed horizontally so top and bottom are longest sides of rectangle.
• Background color or paper color should complement and highlight logo. Do not like a white background. black, grey, brown or any color my logo would blend well with.
Nice to have
• I would like designer to utilize color to highlight letters/name or phone-fax-web symbols.
• Bottom edge of card could be highlighted if appropriate to an idea.
Should not have
• I would NOT want the card to have a pure white background at all.
• No clear cards.
• Cards should be oriented with long sides on bottom and top, NOT sides. DO NOT LIKE THIS THIN TALL ORIENTATION.

```html
<!DOCTYPE html>
<html lang="en">
<head>
<meta charset="utf-8">
<title>Pathbloom Counseling – Business Card</title>
<link rel="stylesheet" href="https://fonts.googleapis.com/css2?family=Arimo:wght@400;700&display=swap">
<style>
  :root {
    --page-bg: #6f7c8a;
    --brand-brown: #5c3d1f;
    --wood-dark: #3a2414;
    --wood-mid: #6a4528;
    --wood-light: #8a5e38;
    --ink-light: #ffffff;
    --ink-soft: #efe6dc;
  }
  * { box-sizing: border-box; margin: 0; padding: 0; }
  html, body {
    width: 1200px; height: 830px; overflow: hidden;
    background: var(--page-bg);
    font-family: "Arimo", Arial, sans-serif;
  }
  .card {
    position: absolute; left: 100px; top: 129px;
    width: 1000px; height: 572px;
    display: flex;
    box-shadow: 0 18px 40px rgba(0,0,0,.35);
  }
  .brand-panel {
    width: 440px; height: 100%;
    background: var(--brand-brown);
    display: flex; align-items: center; justify-content: center;
  }
  .brand-name {
    color: var(--ink-light);
    font-weight: 700; font-size: 44px; line-height: 1.05;
    text-align: center; letter-spacing: .5px;
  }
  .contact-panel {
    position: relative; flex: 1; height: 100%;
    padding: 62px 40px 0 52px;
    color: var(--ink-light);
  }
  .wood-surface {
    position: absolute; inset: 0; z-index: 0;
    background:
      linear-gradient(100deg, rgba(0,0,0,.15), rgba(255,255,255,.04) 45%, rgba(0,0,0,.25)),
      linear-gradient(180deg, var(--wood-light), var(--wood-mid) 45%, var(--wood-dark));
  }
  .contact-content { position: relative; z-index: 1; }
  .person-name { font-size: 29px; font-weight: 700; line-height: 1.15; }
  .person-title { font-size: 21px; line-height: 1.2; color: var(--ink-soft); }
  .contact-list { list-style: none; margin-top: 110px; }
  .contact-item {
    display: flex; align-items: flex-start; gap: 14px;
    font-size: 24px; line-height: 1.25; margin-bottom: 8px;
  }
  .contact-icon { flex: none; width: 28px; height: 28px; margin-top: 2px; }
  .address-lines span { display: block; }
</style>
</head>
<body>
  <div class="card">
    <section class="brand-panel">
      <div class="brand-name">Pathbloom<br>Counseling</div>
    </section>
    <section class="contact-panel">
      <div class="wood-surface" role="img" aria-label="Dark walnut wood grain texture"></div>
      <div class="contact-content">
        <h1 class="person-name">Marcus T. Whitfield, Ph.D.</h1>
        <p class="person-title">Licensed Clinical Psychologist</p>
        <p class="person-title">Integrative Health Coach</p>
        <ul class="contact-list">
          <li class="contact-item">
            <svg class="contact-icon" viewBox="0 0 28 28"><circle cx="14" cy="14" r="14" fill="#fff"/><path d="M14 6a5.5 5.5 0 0 0-5.5 5.5c0 4 5.5 10 5.5 10s5.5-6 5.5-10A5.5 5.5 0 0 0 14 6z" fill="#5c3d1f"/><circle cx="14" cy="11.5" r="2" fill="#fff"/></svg>
            <div class="address-lines"><span>4812 Ferndale Pkwy NW</span><span>Suite 730</span><span>Ashford, GA 30417</span></div>
          </li>
          <li class="contact-item">
            <svg class="contact-icon" viewBox="0 0 28 28"><circle cx="14" cy="14" r="14" fill="#fff"/><path d="M9 7l3 3-2 2.5c1 2 3 4 5.5 5.5l2.5-2 3 3-2 2.5C13 21 7 15 6.5 9z" fill="#5c3d1f"/></svg>
            <span>(770) 555-0142</span>
          </li>
          <li class="contact-item">
            <svg class="contact-icon" viewBox="0 0 28 28"><circle cx="14" cy="14" r="14" fill="#fff"/><rect x="9" y="6.5" width="10" height="5" fill="#5c3d1f"/><rect x="7" y="11" width="14" height="7" rx="1" fill="#5c3d1f"/><rect x="9.5" y="15.5" width="9" height="6" fill="#5c3d1f" stroke="#fff"/></svg>
            <span>(770) 555-0186</span>
          </li>
          <li class="contact-item">
            <svg class="contact-icon" viewBox="0 0 28 28"><circle cx="14" cy="14" r="14" fill="#fff"/><rect x="7" y="9" width="14" height="10" fill="#5c3d1f"/><path d="M7 9l7 6 7-6" fill="none" stroke="#fff" stroke-width="1.3"/></svg>
            <span>drmarcuswhitfield@kelvora.com</span>
          </li>
          <li class="contact-item">
            <svg class="contact-icon" viewBox="0 0 28 28"><circle cx="14" cy="14" r="14" fill="#fff"/><g fill="none" stroke="#5c3d1f" stroke-width="1.5"><circle cx="14" cy="14" r="7"/><ellipse cx="14" cy="14" rx="3" ry="7"/><path d="M7 14h14"/></g></svg>
            <span>pathbloomcounseling.com</span>
          </li>
        </ul>
      </div>
    </section>
  </div>
</body>
</html>
```